Maple Hollow Canine Massage Needs a Business Card Design

Maple Hollow Canine Massage is a new therapeutic canine massage company located in Nederland, Colorado. I need a business card design that include my logo and basic contact information.

Target Market(s)

Pet owners, veterinarians

Industry/Entity Type

Business

Contact Information for Business Card

Lydia Ferrow, CCMT
303.518.7269
lydia@maplehollowmassage.example
www.maplehollowmassage.example

Colors
6c459b
886aae
b8a6cd
a64599
b768aa
d3a5cc
fbed22

Requirements
Must have
• Font should be similar to font in logo.

```html
<!DOCTYPE html>
<html lang="en">
<head>
<meta charset="utf-8">
<title>Maple Hollow Canine Massage – Business Card</title>
<link rel="stylesheet" href="https://fonts.googleapis.com/css2?family=Montserrat:wght@500;600&family=Didact+Gothic&display=swap">
<style>
  :root {
    --backdrop: #d9d9d9;
    --card-white: #f1f0ef;
    --band-light: #8b62a3;
    --panel-dark: #361a47;
    --rail-light: #9d74b4;
    --rail-dark: #3c1f4f;
    --badge-fill: #a07dbd;
    --brand-ink: #3c1f4f;
    --name-ink: #e4dcea;
    --text-ink: #ece6f0;
    --gold: #d8b13a;
  }
  * { box-sizing: border-box; margin: 0; padding: 0; }
  html, body { width: 1200px; height: 899px; overflow: hidden; }
  body {
    background: var(--backdrop);
    display: flex; align-items: center; justify-content: center;
    font-family: "Didact Gothic", sans-serif;
  }
  .business-card {
    position: relative;
    width: 900px; height: 514px;
    display: flex;
    background: var(--card-white);
    box-shadow: 0 12px 30px rgba(0,0,0,.18);
  }
  .brand-side {
    width: 390px;
    display: flex; flex-direction: column; align-items: center; justify-content: center;
    gap: 26px;
  }
  .brand-mark {
    width: 200px; height: 200px; border-radius: 50%;
    background: var(--badge-fill);
  }
  .brand-name {
    font-family: "Montserrat", sans-serif;
    font-weight: 600;
    font-size: 26px;
    line-height: 1.25;
    letter-spacing: .5px;
    text-align: center;
    color: var(--brand-ink);
    text-transform: uppercase;
  }
  .contact-side {
    flex: 1;
    display: flex; flex-direction: column;
  }
  .name-band {
    height: 150px;
    background: var(--band-light);
    display: flex;
  }
  .rail {
    width: 54px; flex: none;
    display: flex; flex-direction: column; align-items: center;
  }
  .name-band .rail { justify-content: flex-end; }
  .rail-cap {
    width: 54px; height: 120px;
    background: var(--rail-dark);
    display: flex; align-items: center; justify-content: center;
  }
  .person-name {
    align-self: flex-end;
    padding: 0 0 30px 26px;
    color: var(--name-ink);
  }
  .person-name h1 {
    font-family: "Montserrat", sans-serif;
    font-weight: 500;
    font-size: 31px;
    letter-spacing: .5px;
    text-transform: uppercase;
    line-height: 1.05;
  }
  .person-name .credential {
    font-size: 22px;
    letter-spacing: 1px;
  }
  .details {
    flex: 1;
    background: var(--panel-dark);
    display: flex;
  }
  .details .rail {
    background: var(--rail-light);
    justify-content: flex-start;
    padding-top: 32px;
    gap: 0;
  }
  .details .rail svg { height: 64px; }
  .contact-list {
    list-style: none;
    padding: 32px 0 0 28px;
  }
  .contact-list li {
    height: 64px;
    display: flex; align-items: center;
    color: var(--text-ink);
    font-size: 21px;
    letter-spacing: .6px;
  }
  .icon { fill: none; stroke: var(--text-ink); stroke-width: 1.6; }
  .icon-solid { fill: var(--text-ink); }
</style>
</head>
<body>
  <main class="business-card">
    <section class="brand-side">
      <div class="brand-mark" aria-hidden="true"></div>
      <p class="brand-name">Maple Hollow<br>Canine Massage</p>
    </section>

    <section class="contact-side">
      <header class="name-band">
        <div class="rail">
          <div class="rail-cap">
            <svg width="24" height="24" viewBox="0 0 24 24" aria-hidden="true">
              <circle class="icon-solid" cx="12" cy="8" r="5"/>
              <path class="icon-solid" d="M2 22c0-6 4.5-8.5 10-8.5S22 16 22 22z"/>
            </svg>
          </div>
        </div>
        <div class="person-name">
          <h1>Lydia Ferrow</h1>
          <p class="credential">CCMT</p>
        </div>
      </header>

      <div class="details">
        <div class="rail" aria-hidden="true">
          <svg width="26" viewBox="0 0 26 64">
            <path class="icon-solid" d="M6 22c2-2 4-2 5 0l2 3c1 1.5 0 3-1 3.5-.5.5 0 2 2 4.5s4 3 4.5 2.5c.5-1 2-2 3.5-1l3 2c1.5 1 1.5 3 0 4.5-3 3-8 1-13-4S3 25 6 22z"/>
          </svg>
          <svg width="26" viewBox="0 0 26 64">
            <circle class="icon" cx="13" cy="32" r="11"/>
            <ellipse class="icon" cx="13" cy="32" rx="5" ry="11"/>
            <path class="icon" d="M2 32h22M4 26h18M4 38h18"/>
          </svg>
          <svg width="26" viewBox="0 0 26 64">
            <rect class="icon" x="2" y="24" width="22" height="16"/>
            <path class="icon" d="M2 24l11 9 11-9M2 40l8-8M24 40l-8-8"/>
          </svg>
        </div>
        <ul class="contact-list">
          <li>303.518.7269</li>
          <li>www.maplehollowmassage.example</li>
          <li>lydia@maplehollowmassage.example</li>
        </ul>
      </div>
    </section>
  </main>
</body>
</html>
```